Carewell Hub Needs a Web Design

Designers will use (and improve) our mockups to re-design our mobile-friendly website. We would like to see designs that use the color blue (as our logo in the attached file). The final design should convey convenience and communicate accessible health and wellness.

We need a web design for a company based in Kampala called 'Carewell Hub'.

We help patients to compare health insurance, find a doctor and book an appointment instantly.

Our initial products are Find and Book - a Wordpress database that helps patients to find a doctor and book an appointment instantly; and Insurance - a database that helps patients compare health insurance policies online. We would like to see designs that are mobile-friendly and responsive with awesome user interface and experience.
Updates

Project Deadline Extended Reason: We need web design of 5+ pages. Please see attached files for guidance. Added Wednesday, February 17, 2016

Industry/Entity Type

Health Service

Number of Pages Required

5+ page

Font styles to use
Sans Serif

Colors
33a6d7
85cae6
cee9f5
ecf7fb

Requirements
Must have
• Mobile-friendly and responsive design with awesome UI and UX

```html
<!DOCTYPE html>
<html lang="en">
<head>
<meta charset="utf-8">
<title>Carewell Hub – Lakeview College Health Center</title>
<link href="https://fonts.googleapis.com/css2?family=Open+Sans:wght@400;600;700&display=swap" rel="stylesheet">
<style>
:root{
  --blue:#33a6d7;
  --ink:#333;
  --muted:#777;
  --line:#e4e4e4;
  --panel:#f2f2f2;
  --dark:#2b2b2b;
  --bar:#4a4a4a;
  --footer:#f7f7f7;
}
*{box-sizing:border-box;margin:0;padding:0}
html,body{width:825px;height:1200px;overflow:hidden}
body{position:relative;background:#fff;font-family:"Open Sans",Arial,sans-serif;color:var(--ink);font-size:7px}
.abs{position:absolute}
a{color:inherit;text-decoration:none}

.nav-link{font-size:7px;font-weight:600;color:#444;top:21px}
.brand{left:360px;top:15px;font-size:13px;font-weight:700;color:var(--blue);display:flex;align-items:center;gap:5px}
.brand i{width:10px;height:10px;border-radius:50%;background:var(--blue);display:block}
.btn-insurance{left:518px;top:16px;width:54px;height:18px;background:var(--blue);color:#fff;font-weight:700;font-size:7px;display:flex;align-items:center;justify-content:center}
.auth{left:583px;top:21px;font-size:7px;font-weight:600;color:#444}

.hero{left:0;top:50px;width:825px;height:86px;background:linear-gradient(100deg,#2a2a2a,#4a4a4a 55%,#333)}
.loc-box{left:184px;top:80px;width:115px;height:28px;background:#fff;border:2px solid var(--blue);display:flex;align-items:center;padding-left:8px;gap:6px;font-size:8px;color:#666}
.search-box{left:305px;top:80px;width:271px;height:28px;background:#fff;border:2px solid var(--blue);display:flex;align-items:center;padding-left:9px;gap:8px;font-size:7.5px;color:#999}
.btn-find{left:575px;top:80px;width:63px;height:28px;background:var(--blue);color:#fff;font-weight:600;font-size:8px;display:flex;align-items:center;justify-content:center}

.crumbs{left:0;top:136px;width:825px;height:20px;border-bottom:1px solid var(--line);padding-left:184px;display:flex;align-items:center;gap:8px;font-size:6px;color:#666}
.crumbs span.sep{color:#bbb}

.card{left:184px;top:177px;width:329px;height:316px;border:1px solid var(--line)}
.profile-img{left:196px;top:195px;width:88px;height:66px;background:#eee;border:1px solid #ddd}
.clinic-title{left:296px;top:193px;font-size:8.5px;color:var(--blue);font-weight:400}
.meta{left:296px;font-size:6px;color:#555;display:flex;align-items:center;gap:6px}
.share-chip{height:7px;border:1px solid #cdd;background:#eef3f8;display:inline-block;margin-right:2px}
.tabs{left:184px;top:290px;width:329px;height:22px;background:#f5f5f5;border-top:1px solid var(--line);border-bottom:1px solid var(--line);display:flex}
.tab{font-size:6.5px;color:#444;display:flex;align-items:center;justify-content:center}
.tab.active{background:#fff;color:var(--blue);border-right:1px solid var(--line);height:22px;margin-top:-1px}
.section-h{font-size:7px;color:#555;letter-spacing:.2px}
.about{left:200px;top:343px;width:302px;font-size:5.4px;line-height:9.5px;color:#444}
.svc{font-size:5.6px;color:#555}
.rule{height:1px;background:var(--line)}
.ph{width:45px;height:32px;background:#eee;border:1px solid #e2e2e2}

.doc-bar{left:184px;top:507px;width:329px;height:21px;background:var(--bar);color:#fff;font-size:8px;font-weight:400;padding-left:9px;display:flex;align-items:center}
.doc-row{left:184px;width:329px;height:98px;border-bottom:1px solid var(--line)}
.doc-photo{position:absolute;left:0;top:14px;width:79px;height:54px;background:linear-gradient(135deg,#5a6878,#3c4a5c 60%,#6d7f96)}
.doc-name{position:absolute;left:90px;top:14px;font-size:8px;font-weight:600;color:#333}
.doc-info{position:absolute;left:90px;top:36px;font-size:5.8px;color:#777;line-height:12.5px}
.doc-side{position:absolute;left:193px;top:0;width:136px;height:97px;background:var(--panel)}
.doc-side .row{position:absolute;left:33px;font-size:5.8px;color:#333;display:flex;align-items:center;gap:6px}
.btn-instant,.btn-book{position:absolute;top:72px;height:15px;color:#fff;font-size:5.2px;font-weight:700;display:flex;align-items:center;justify-content:center}
.btn-instant{left:10px;width:45px;background:var(--blue)}
.btn-book{left:55px;width:75px;background:var(--dark)}

.report{left:457px;top:846px;font-size:6.2px;color:#777}
.partner{left:214px;top:890px;width:270px;text-align:center;font-size:20px;font-weight:600;color:#555}
.partner-tag{left:214px;top:922px;width:270px;text-align:center;font-size:8px;color:#555}
.related{left:183px;top:969px;width:330px;height:81px;background:var(--dark);padding:22px 0 0 21px;font-size:6.6px;color:#9a9a9a;line-height:15px}

.side{left:523px;top:177px;width:116px;height:201px;border:1px solid var(--line);background:#f5f5f5}
.app-visual{left:550px;top:195px;width:60px;height:113px;background:linear-gradient(180deg,#1a1a1a,#2e2e2e)}
.mobile-input{left:532px;top:320px;width:99px;height:19px;background:#fff;border:1px solid var(--line);font-size:6px;color:#777;padding-left:9px;display:flex;align-items:center}
.btn-send{left:532px;top:345px;width:99px;height:21px;background:#333;color:#fff;font-size:5.4px;font-weight:600;display:flex;align-items:center;justify-content:center}

.footer{left:0;top:1067px;width:825px;height:91px;background:var(--footer)}
.fcol{top:1083px;font-size:6.2px;color:#555;line-height:15px}
.fcol h4{font-size:6.4px;font-weight:600;color:#444;letter-spacing:.3px;margin-bottom:2px}
.fcol .ico{display:inline-block;width:6px;height:6px;border-radius:50%;background:#666;margin-right:6px;vertical-align:-1px}
.copy{left:183px;top:1169px;font-size:5px;color:#666}
</style>
</head>
<body>

<header>
  <a class="abs nav-link" style="left:184px" href="#">CWH for Doctors</a>
  <a class="abs nav-link" style="left:266px" href="#">Blog</a>
  <div class="abs brand"><i></i>Carewell Hub</div>
  <a class="abs btn-insurance" href="#">Insurance</a>
  <div class="abs auth">Login &nbsp;|&nbsp; Register</div>
</header>

<div class="abs hero" role="img" aria-label="Dark photo of a stethoscope on medical paperwork"></div>
<div class="abs loc-box">
  <svg width="8" height="11" viewBox="0 0 8 11"><path d="M4 0a4 4 0 0 0-4 4c0 3 4 7 4 7s4-4 4-7a4 4 0 0 0-4-4z" fill="#999"/><circle cx="4" cy="4" r="1.5" fill="#fff"/></svg>
  <span style="flex:1">Kampala</span>
  <svg width="6" height="4" style="margin-right:10px"><path d="M0 0h6L3 4z" fill="#777"/></svg>
</div>
<div class="abs search-box">
  <svg width="11" height="11" viewBox="0 0 11 11"><circle cx="4.5" cy="4.5" r="3.5" stroke="#999" stroke-width="1.5" fill="none"/><path d="M7 7l3.5 3.5" stroke="#999" stroke-width="1.8"/></svg>
  Specialities, Doctors, Clinics, Labs, etc
</div>
<a class="abs btn-find" href="#">Find Doctor</a>

<nav class="abs crumbs">
  <span>Home</span><span class="sep">›</span><span>Kampala Clinics</span><span class="sep">›</span><span>Palm Road</span><span class="sep">›</span><span>Lakeview College Health Center</span>
</nav>

<section class="abs card"></section>
<div class="abs profile-img" role="img" aria-label="Clinic photo placeholder"></div>
<h1 class="abs clinic-title">Lakeview College Health Center Dermatologist</h1>
<div class="abs meta" style="top:216px">
  <svg width="7" height="9" viewBox="0 0 8 11"><path d="M4 0a4 4 0 0 0-4 4c0 3 4 7 4 7s4-4 4-7a4 4 0 0 0-4-4z" fill="#888"/><circle cx="4" cy="4" r="1.5" fill="#fff"/></svg>
  Plot NO: 31, Palm Road, Kampala
</div>
<div class="abs meta" style="top:234px">
  <svg width="9" height="9"><circle cx="4.5" cy="4.5" r="3.8" stroke="#888" fill="none"/><path d="M4.5 2v2.7h2" stroke="#888" fill="none"/></svg>
  Mon-Fri &nbsp;10:00am - 2:00pm, 5:00pm - 8:00pm
</div>
<div class="abs meta" style="top:253px">
  <svg width="9" height="9"><circle cx="2" cy="4.5" r="1.5" fill="#888"/><circle cx="7" cy="1.8" r="1.5" fill="#888"/><circle cx="7" cy="7.2" r="1.5" fill="#888"/><path d="M2 4.5L7 1.8M2 4.5L7 7.2" stroke="#888"/></svg>
  <span><span class="share-chip" style="width:20px"></span><span class="share-chip" style="width:9px;background:#fff"></span><span class="share-chip" style="width:24px"></span><span class="share-chip" style="width:13px;background:#fff"></span><span class="share-chip" style="width:14px"></span><span class="share-chip" style="width:11px;background:#fff"></span><span class="share-chip" style="width:20px;background:#e85a40;border-color:#e85a40"></span><span class="share-chip" style="width:14px;background:#fff"></span></span>
</div>

<div class="abs tabs">
  <div class="tab active" style="width:60px">Overview</div>
  <div class="tab" style="width:45px">Doctors</div>
  <div class="tab" style="width:68px">Feedback ( 0 )</div>
  <div class="tab" style="width:42px">Photos</div>
  <div class="tab" style="width:50px">Services</div>
  <div class="tab" style="width:38px">Map</div>
</div>

<div class="abs section-h" style="left:202px;top:327px">ABOUT</div>
<p class="abs about">Lorem ipsum dolor sit amet, consectetur adipiscing elit, sed do eiusmod tempor incididunt ut labore et dolore magna aliqua. Ut enim ad minim veniam, quis nostrud exercitation ullamco laboris nisi ut aliquip ex ea commodo consequat. Duis aute irure dolor in reprehenderit in voluptate velit esse cillum dolore eu fugiat nulla pariatur.</p>

<div class="abs section-h" style="left:200px;top:392px;display:flex;align-items:center;gap:6px">
  <svg width="9" height="9"><rect x=".5" y=".5" width="8" height="8" fill="none" stroke="#777"/><path d="M4.5 2v5M2 4.5h5" stroke="#777"/></svg>SERVICES
</div>
<div class="abs rule" style="left:200px;top:408px;width:143px"></div>
<div class="abs svc" style="left:200px;top:416px;line-height:15px">Child Immunization<br>Dermatologist<br>ENT Doctor</div>
<div class="abs svc" style="left:284px;top:416px;line-height:15px">Dieticians<br>Root Canals<br>Weight Loss</div>

<div class="abs section-h" style="left:360px;top:392px;display:flex;align-items:center;gap:6px">
  <svg width="11" height="9"><rect x=".5" y="1.5" width="10" height="7" fill="none" stroke="#777"/><circle cx="5.5" cy="5" r="1.8" fill="none" stroke="#777"/></svg>PHOTOS
</div>
<div class="abs rule" style="left:360px;top:408px;width:144px"></div>
<div class="abs ph" style="left:361px;top:415px"></div>
<div class="abs ph" style="left:410px;top:415px"></div>
<div class="abs ph" style="left:459px;top:415px"></div>
<div class="abs ph" style="left:361px;top:453px"></div>
<div class="abs ph" style="left:410px;top:453px"></div>
<div class="abs ph" style="left:459px;top:453px"></div>

<h2 class="abs doc-bar">Doctors</h2>

<article class="abs doc-row" style="top:534px">
  <div class="doc-photo" role="img" aria-label="Portrait photo of the doctor"></div>
  <div class="doc-name">Dr. Tom Reed</div>
  <div class="doc-info">MBChB, MBBS<br>10 Years Experience<br>Dermatologist</div>
  <div class="doc-side">
    <div class="row" style="top:15px;font-weight:600"><svg width="9" height="7"><rect width="9" height="6" rx="1" fill="#666"/></svg>( 31 ) Feedback</div>
    <div class="row" style="top:30px;font-weight:700"><svg width="9" height="9"><circle cx="4.5" cy="4.5" r="3.8" stroke="#666" fill="none"/><path d="M4.5 2v2.7h2" stroke="#666" fill="none"/></svg>Mon-Fri, Sat</div>
    <div class="row" style="top:43px;left:48px">10:00am - 2:00pm</div>
    <div class="row" style="top:56px;left:48px">5:00pm - 8:00pm</div>
    <a class="btn-instant" href="#">INSTANT</a><a class="btn-book" href="#">BOOK APPOINTMENT</a>
  </div>
</article>

<article class="abs doc-row" style="top:638px">
  <div class="doc-photo" role="img" aria-label="Portrait photo of the doctor"></div>
  <div class="doc-name">Dr. Tom Reed</div>
  <div class="doc-info">MBChB, MBBS<br>10 Years Experience<br>Dermatologist</div>
  <div class="doc-side">
    <div class="row" style="top:15px;font-weight:600"><svg width="9" height="7"><rect width="9" height="6" rx="1" fill="#666"/></svg>( 31 ) Feedback</div>
    <div class="row" style="top:30px;font-weight:700"><svg width="9" height="9"><circle cx="4.5" cy="4.5" r="3.8" stroke="#666" fill="none"/><path d="M4.5 2v2.7h2" stroke="#666" fill="none"/></svg>Mon-Fri, Sat</div>
    <div class="row" style="top:43px;left:48px">10:00am - 2:00pm</div>
    <div class="row" style="top:56px;left:48px">5:00pm - 8:00pm</div>
    <a class="btn-instant" href="#">INSTANT</a><a class="btn-book" href="#">BOOK APPOINTMENT</a>
  </div>
</article>

<article class="abs doc-row" style="top:742px">
  <div class="doc-photo" role="img" aria-label="Portrait photo of the doctor"></div>
  <div class="doc-name">Dr. Tom Reed</div>
  <div class="doc-info">MBChB, MBBS<br>10 Years Experience<br>Dermatologist</div>
  <div class="doc-side">
    <div class="row" style="top:15px;font-weight:600"><svg width="9" height="7"><rect width="9" height="6" rx="1" fill="#666"/></svg>( 31 ) Feedback</div>
    <div class="row" style="top:30px;font-weight:700"><svg width="9" height="9"><circle cx="4.5" cy="4.5" r="3.8" stroke="#666" fill="none"/><path d="M4.5 2v2.7h2" stroke="#666" fill="none"/></svg>Mon-Fri, Sat</div>
    <div class="row" style="top:43px;left:48px">10:00am - 2:00pm</div>
    <div class="row" style="top:56px;left:48px">5:00pm - 8:00pm</div>
    <a class="btn-instant" href="#">INSTANT</a><a class="btn-book" href="#">BOOK APPOINTMENT</a>
  </div>
</article>

<a class="abs report" href="#">Report an Error</a>
<div class="abs rule" style="left:184px;top:861px;width:329px"></div>

<div class="abs partner">FindCareNow</div>
<div class="abs partner-tag">Connecting Patients &amp; Doctors Worldwide</div>

<div class="abs related">Related Clinics in Kampala<br>Maple Children's Medical Center<br>The Hillside Medical Center</div>

<aside class="abs side"></aside>
<div class="abs app-visual" role="img" aria-label="Illustration of a phone promoting the free Carewell Hub app with store badges"></div>
<div class="abs mobile-input">Enter your mobile Number</div>
<a class="abs btn-send" href="#">SEND ME APPS LINK</a>

<footer class="abs footer"></footer>
<div class="abs fcol" style="left:183px"><h4>CAREWELL HUB</h4>Search for Doctor<br>Search For clinic</div>
<div class="abs fcol" style="left:272px"><h4>FOR DOCTORS</h4>List your Clinic</div>
<div class="abs fcol" style="left:349px"><h4>SUPPORT</h4>Contact Us</div>
<div class="abs fcol" style="left:423px"><h4>ABOUT US</h4>Our Story<br>Blog</div>
<div class="abs fcol" style="left:496px"><h4>CONNECT</h4><span class="ico"></span>Chirpline<br><span class="ico"></span>Friendbook<br><span class="ico"></span>Circleup</div>
<div class="abs fcol" style="left:575px"><h4>MORE</h4>Privacy Policy<br>Terms &amp; Condition</div>
<div class="abs copy">© Copyright 2016 Carewell Hub Limited. All rights reserved.</div>

</body>
</html>
```